Gorgeous A5 Booklet 8pp - Existing Branding

Please transform a PDF text doc into an A5 booklet according to my existing branding, I need it fast.
I need to go to print.
Must be modern, fun, clean and classy design.
I can send images, logos and the .indd for the existing pdf to help you.
Thanks for being awesome!

We are a design agency so it needs to be good...we are too busy to create it.

Front cover can have open paragraph.
Back cover must have contact details
three inside spreads should have the 11 essentials.

The executive summary attached is a good example of the look and feel you can copy.

Please let me know if you have any questions.
Thanks
Light ahead!
:)

Target Market(s)

entreprenuers and small business owners

Industry/Entity Type

Design Agency

Font styles to use
Sans Serif

Colors
e34197
fff5ee
333333
faa54b
acd036
33a6d7

Requirements
Must have
• font is century gothic - no bold
gudea body text
sketch rockwell
seans hand

see website www.brightvane.com.au for branding
or match to pdf attached with origami images

Colours in palette below of only indicative. actual colours are as per website colour strip.
Should not have
• not too pink
not too many stars

```html
<!DOCTYPE html>
<html lang="en">
<head>
<meta charset="utf-8">
<title>11 Essentials for a Successful Website – Booklet Spread</title>
<link rel="stylesheet" href="https://fonts.googleapis.com/css2?family=Gudea:wght@400&family=Roboto+Slab:wght@400;600&family=Questrial&display=swap">
<style>
  :root {
    --pink: #e34197;
    --green: #acd036;
    --orange: #faa54b;
    --blue: #33a6d7;
    --ink: #333333;
    --paper: #ffffff;
    --linen: #ebe6df;
    --desk: #c9c9c9;
  }
  * { box-sizing: border-box; margin: 0; padding: 0; }
  html, body { width: 1200px; height: 738px; overflow: hidden; background: var(--desk); }
  .spread { position: relative; width: 1200px; height: 738px; }
  .page {
    position: absolute; top: 0; width: 520px; height: 738px;
    background: var(--paper);
    font-family: "Gudea", sans-serif; color: var(--ink);
  }
  .page--left { left: 17px; }
  .page--right { left: 646px; }
  .page__header {
    position: absolute; left: 0; top: 0; width: 100%; height: 320px;
    background: var(--linen);
  }
  .page__photo { position: absolute; top: 0; left: 34px; width: 452px; height: 320px; }
  .page--left .page__photo {
    background: linear-gradient(100deg, #e8eef0 0%, #f7f7f5 40%, #f2eeea 70%, #dfe3e4 100%);
  }
  .page--right .page__photo {
    background: linear-gradient(110deg, #e9ecee 0%, #f4f1ec 35%, #b9cfd2 60%, #e7e4e0 100%);
  }
  .page__title {
    position: absolute; left: 46px; top: 248px;
    font-family: "Roboto Slab", serif; color: var(--ink); line-height: 1.1;
  }
  .page__title-lead { display: block; font-size: 16px; font-weight: 600; }
  .page__title-main { display: block; font-size: 25px; font-weight: 600; }
  .page--right .page__title { top: 252px; }
  .page--right .page__title-main { font-size: 17px; }
  .stripe { position: absolute; left: 0; width: 100%; height: 5px; display: flex; }
  .stripe span { flex: 1; }
  .stripe .s-pink { background: var(--pink); flex: 1.2; }
  .stripe .s-green { background: var(--green); }
  .stripe .s-orange { background: var(--orange); flex: 0.8; }
  .stripe .s-blue { background: var(--blue); flex: 1.3; }
  .stripe--top { top: 320px; }
  .stripe--bottom { top: 733px; }
  .essentials {
    position: absolute; top: 330px; left: 12px; right: 12px;
    list-style: none; font-size: 12.9px; line-height: 19.6px;
  }
  .essential { position: relative; padding-left: 18px; margin-bottom: 2px; }
  .essential__num { position: absolute; left: 0; top: 0; color: var(--pink); }
  .essential__head { color: var(--pink); }
  .essential p + p { margin-top: 0; }
  .essential__more { padding-left: 12px; margin-top: 4px; }
  .brand {
    position: absolute; top: 700px;
    font-family: "Questrial", sans-serif; font-size: 17px; color: var(--pink);
  }
  .page--left .brand { left: 12px; }
  .page--right .brand { right: 12px; }
</style>
</head>
<body>
<main class="spread">

  <section class="page page--left">
    <header class="page__header">
      <div class="page__photo" role="img" aria-label="Photo of a smiling woman in a white chef jacket in a bright kitchen"></div>
      <h1 class="page__title">
        <span class="page__title-lead">11 Essentials for a</span>
        <span class="page__title-main">Successful website</span>
      </h1>
    </header>
    <div class="stripe stripe--top"><span class="s-pink"></span><span class="s-green"></span><span class="s-orange"></span><span class="s-blue"></span></div>

    <ol class="essentials">
      <li class="essential">
        <span class="essential__num">1.</span>
        <p>Perfect Elevator Pitch Studies show that website visitors spend an average of seven seconds or less on 90% of the websites they visit. This means you only have a few precious moments to convey who you are, what you do, who you do it for, and why you're the best choice. Make sure you nail your pitch and get in front and center on your homepage.</p>
        <p>It's important to spend time honing your core marketing message and ensuring that your logo, tagline and the initial two sentences of your website copy are clear and present your brand with credibility and impact succinctly outlining your specialty and target niche. There's a lot to communicate in very little time so your pitch must be concise and compelling.</p>
      </li>
      <li class="essential">
        <span class="essential__num">2.</span>
        <p>Clear Call to Actions When small business owners ask, "Why isn't my website converting?" the answer is most often a lack of call to actions. Common call to actions include phone numbers and "Buy Now" buttons, but they may also be more subtle actions encouraging visitors to a next step. Call to actions are designed to engage your visitors and guide them down the path to a conversion. Visitors to your website need specific information before committing to a purchase or enquiry, smart call to actions preempt the visitors next step and gently lead them through your website in the way you want them to experience your website while delivering the information they are seeking.</p>
      </li>
    </ol>

    <div class="brand">brightvane</div>
    <div class="stripe stripe--bottom"><span class="s-pink"></span><span class="s-green"></span><span class="s-orange"></span><span class="s-blue"></span></div>
  </section>

  <section class="page page--right">
    <header class="page__header">
      <div class="page__photo" role="img" aria-label="Photo of two men reviewing paperwork together at a desk in an office"></div>
      <h2 class="page__title">
        <span class="page__title-main">11 Essentials for a</span>
        <span class="page__title-main">Successful website</span>
      </h2>
    </header>
    <div class="stripe stripe--top"><span class="s-pink"></span><span class="s-green"></span><span class="s-orange"></span><span class="s-blue"></span></div>

    <ol class="essentials">
      <li class="essential">
        <span class="essential__num">3.</span>
        <p><span class="essential__head">Track your Conversations:</span> We mention conversion tracking up the top because it's so often neglected, yet it's one of the easiest strategies to implement. It is vital to know how many enquiries and sales that you receive through your website, where those website visitors come from and what the cost is to acquire them. This allows you to accurately measure your marketing spend, evaluate the success of any improvements or modifications in your website design or online marketing, and ultimately measure the underlying success of your website.</p>
      </li>
      <li class="essential">
        <span class="essential__num">4.</span>
        <p><span class="essential__head">Engaging "About Us" Page:</span> The two biggest mistakes made with About Us pages is that they are often boring, and they're not about the customer. It may seem counter-intuitive to write an About Us page that is more about your customer than your company, but there's a good reason for it.</p>
        <p class="essential__more">Your company exists for your customer. So by logical extension, your About Us page is also about your customer. That's not to say it shouldn't create an engaging portrait of the personalities behind your organisation because your prospects want to know who they're working with, but they also want to know how those people are going to make their lives better. Your About Us page, like the rest of your website, should present all information in the context of how it benefits your visitors.</p>
      </li>
    </ol>

    <div class="brand">brightvane</div>
    <div class="stripe stripe--bottom"><span class="s-pink"></span><span class="s-green"></span><span class="s-orange"></span><span class="s-blue"></span></div>
  </section>

</main>
</body>
</html>
```